Keystone Title Transfers

We are a legal service provider.
We deal predominately with Real Estate title transfers.
We will be printing on white paper with black ink, so colour is not really needed for the letter head.

I have enclosed our logo which i will like to be incorporated into the letterhead.

I have also attached a copy of our current old letterhead with all our office details on there. Everything that is listed in the current letterhead i would like to be included in the new one.

Target Market(s)

Real Estate, Home buyers & Sellers, Solicitors and Lawyers, Pest & Building Inspectors

Industry/Entity Type

Legal

Font styles to use
Serif

Requirements
Must have
• Simple and Legal looking.

```html
<!DOCTYPE html>
<html lang="en">
<head>
<meta charset="utf-8">
<title>Keystone Title Transfers — Letterhead</title>
<link rel="stylesheet" href="https://fonts.googleapis.com/css2?family=Lora:wght@400;700&display=swap">
<style>
  :root {
    --paper: #ffffff;
    --ink: #3f3f3f;
    --ink-soft: #555555;
    --accent: #9b2a2e;
    --card-border: #8a8a8a;
  }
  * { margin: 0; padding: 0; box-sizing: border-box; }
  html, body { width: 851px; height: 1200px; overflow: hidden; background: var(--paper); }
  .letterhead {
    position: relative;
    width: 851px;
    height: 1200px;
    background: var(--paper);
    font-family: "Lora", Georgia, serif;
    color: var(--ink);
  }
  .brand {
    position: absolute;
    display: flex;
    align-items: center;
    gap: 12px;
  }
  .brand-mark { background: var(--accent); flex: none; }
  .brand-name {
    font-weight: 700;
    color: var(--ink);
    text-transform: uppercase;
    line-height: 1.05;
  }
  .letterhead > .brand { left: 57px; top: 62px; }
  .letterhead > .brand .brand-mark { width: 30px; height: 30px; }
  .letterhead > .brand .brand-name { font-size: 30px; letter-spacing: 1px; }

  .business-card {
    position: absolute;
    left: 431px;
    top: 558px;
    width: 363px;
    height: 179px;
    border: 1px solid var(--card-border);
    background: var(--paper);
    padding: 28px 30px;
  }
  .business-card .brand { position: static; gap: 7px; }
  .business-card .brand-mark { width: 14px; height: 14px; }
  .business-card .brand-name { font-size: 15px; letter-spacing: 0.5px; }
  .card-details {
    display: flex;
    gap: 46px;
    margin-top: 26px;
    font-size: 11px;
    line-height: 1.45;
    color: var(--ink-soft);
  }
  .card-name { color: var(--accent); }

  .footer-contact {
    position: absolute;
    left: 57px;
    top: 1128px;
    font-size: 15px;
    color: var(--ink);
    white-space: nowrap;
    word-spacing: 1px;
  }
  .footer-contact span + span { margin-left: 14px; }
</style>
</head>
<body>
<main class="letterhead">
  <header class="brand">
    <span class="brand-mark"></span>
    <span class="brand-name">Keystone<br>Title Transfers</span>
  </header>

  <section class="business-card">
    <div class="brand">
      <span class="brand-mark"></span>
      <span class="brand-name">Keystone<br>Title Transfers</span>
    </div>
    <div class="card-details">
      <div>
        <div class="card-name">Name Here</div>
        <div>Email@web.com</div>
        <div>000-000-0000</div>
      </div>
      <div>
        <div>Address Line One</div>
        <div>Address Line Two</div>
        <div>City State 000000</div>
        <div>webaddress.com</div>
      </div>
    </div>
  </section>

  <footer class="footer-contact">
    <span>Address Line One, Address Line Two, City State 000000</span>
    <span>phone number</span>
    <span>webaddress.com</span>
  </footer>
</main>
</body>
</html>
```